KLT Roofing Pty Ltd

We are a high end residential Roofing company
We would like something silimar to the attached logo with the same color scheme

Target Market(s)

High end residential Builders & Architects

Industry/Entity Type

Residential

```html
<!DOCTYPE html>
<html lang="en">
<head>
<meta charset="utf-8">
<title>KLT Roofing – Business Card</title>
<link rel="stylesheet" href="https://fonts.googleapis.com/css2?family=Open+Sans:wght@400;600;700&display=swap">
<style>
  :root {
    --bg: #ecebe8;
    --card: #ffffff;
    --slate: #56636e;
    --slate-dark: #46525c;
    --blue: #1fa3d6;
    --ink: #3d4850;
    --shadow: 0 6px 18px rgba(0,0,0,0.18);
  }
  * { box-sizing: border-box; margin: 0; padding: 0; }
  html, body {
    width: 1200px; height: 913px; overflow: hidden;
    background: var(--bg);
    font-family: "Open Sans", Arial, sans-serif;
  }
  .canvas { position: relative; width: 1200px; height: 913px; }

  .card {
    position: absolute;
    width: 540px; height: 310px;
    background: var(--card);
    box-shadow: var(--shadow);
    overflow: hidden;
  }
  .card--front { left: 60px; top: 130px; }
  .card--back  { left: 600px; top: 470px; }

  /* wordmark */
  .wordmark { display: flex; align-items: center; gap: 12px; }
  .wordmark__square { width: 22px; height: 22px; background: var(--slate); }
  .wordmark__name {
    font-weight: 700; color: var(--slate);
    letter-spacing: 2px; text-transform: uppercase;
  }
  .card--front .wordmark {
    position: absolute; left: 50%; top: 50%;
    transform: translate(-50%, -50%);
  }
  .card--front .wordmark__name { font-size: 40px; }
  .card--front .wordmark__square { width: 34px; height: 34px; }

  .card--back .wordmark { position: absolute; left: 34px; top: 118px; }
  .card--back .wordmark__name { font-size: 28px; }

  /* person */
  .person { position: absolute; right: 34px; top: 42px; text-align: right; }
  .person__name {
    font-size: 19px; font-weight: 700; color: var(--slate);
    letter-spacing: 1px; text-transform: uppercase; line-height: 1.1;
  }
  .person__role { font-size: 13px; color: var(--blue); line-height: 1.3; }
  .person__rule {
    width: 200px; height: 1px; background: var(--slate);
    margin-left: auto; margin-top: 3px;
  }

  /* contact */
  .contact { position: absolute; left: 34px; top: 200px; width: 320px; }
  .contact__rule { height: 1px; background: var(--slate); margin-bottom: 6px; }
  .contact__line {
    display: flex; align-items: center; gap: 8px;
    font-size: 12px; color: var(--ink); line-height: 17px;
  }
  .contact__line svg { width: 11px; height: 11px; fill: var(--slate-dark); flex: none; }

  /* bottom band */
  .band { position: absolute; left: 0; right: 0; bottom: 0; }
  .band__accent { height: 4px; background: var(--blue); }
  .band__base { height: 24px; background: var(--slate); }
</style>
</head>
<body>
<main class="canvas">

  <section class="card card--front" aria-label="Card front">
    <div class="wordmark">
      <span class="wordmark__square"></span>
      <span class="wordmark__name">KLT Roofing</span>
    </div>
  </section>

  <section class="card card--back" aria-label="Card back">
    <div class="person">
      <p class="person__name">Jordan Callister</p>
      <div class="person__rule"></div>
      <p class="person__role">General Manager</p>
    </div>

    <div class="wordmark">
      <span class="wordmark__square"></span>
      <span class="wordmark__name">KLT Roofing</span>
    </div>

    <div class="contact">
      <div class="contact__rule"></div>
      <p class="contact__line">
        <svg viewBox="0 0 12 12" aria-hidden="true"><path d="M2.5 0.8 L4.6 3.2 L3.6 4.5 Q4.7 6.9 7.4 8.3 L8.7 7.3 L11.2 9.4 L10 11.2 Q3.8 11 0.8 2 Z"/></svg>
        0400 555 019
      </p>
      <p class="contact__line">
        <svg viewBox="0 0 12 12" aria-hidden="true"><path d="M0.5 2.5 H11.5 V10 H0.5 Z M1.2 3 L6 6.6 L10.8 3 Z" fill-rule="evenodd"/></svg>
        jcallister@kltroofing.com.au
      </p>
      <p class="contact__line">
        <svg viewBox="0 0 12 12" aria-hidden="true"><path d="M6 0.5 A3.8 3.8 0 0 1 9.8 4.3 C9.8 7 6 11.5 6 11.5 C6 11.5 2.2 7 2.2 4.3 A3.8 3.8 0 0 1 6 0.5 Z"/></svg>
        12 Harbour Lane, Port Bayside
      </p>
    </div>

    <div class="band">
      <div class="band__accent"></div>
      <div class="band__base"></div>
    </div>
  </section>

</main>
</body>
</html>
```